TEK Logistics - Banner 2.5' x 8' for 20+ locations

Need a banner designed that will pop. This banner will be displayed at over 20 of our transportation facilities. Goal is for the banner to grab the attention of employees, contractors and clients and help reinforce our mission and core values. Designed needs to include TEK Logo, our core values and mission statement. Red and Black are the main company colors and we need to stay within that theme and color pallet. Attached is a previous version that was too basic and boring. Willing to consider a design that excludes the mission statement.

Gathering more feedback

```html
<!DOCTYPE html>
<html lang="en">
<head>
<meta charset="utf-8">
<title>TEK Logistics – Core Values Banner</title>
<link href="https://fonts.googleapis.com/css2?family=Barlow+Condensed:wght@600&display=swap" rel="stylesheet">
<style>
  :root {
    --page-bg: #dcdcdc;
    --banner-black: #151515;
    --banner-charcoal: #2a2a2a;
    --brand-red: #d0302a;
    --brand-red-dark: #9e2420;
    --text-white: #ffffff;
    --text-grey: #cfcfcf;
    --photo-light: #b9b9b9;
    --photo-dark: #4a4a4a;
  }
  * { margin: 0; padding: 0; box-sizing: border-box; }
  html, body {
    width: 1200px;
    height: 938px;
    overflow: hidden;
    background: var(--page-bg);
    font-family: "Barlow Condensed", "Arial Narrow", sans-serif;
    font-weight: 600;
  }
  .banner {
    position: absolute;
    left: 20px;
    top: 275px;
    width: 1160px;
    height: 387px;
    background: linear-gradient(120deg, var(--banner-black) 0%, var(--banner-charcoal) 45%, var(--banner-black) 100%);
    overflow: hidden;
  }
  .banner__accent {
    position: absolute;
    inset: 0;
    width: 100%;
    height: 100%;
  }
  .core-values {
    position: absolute;
    left: 24px;
    top: 30px;
    list-style: none;
    font-size: 28px;
    line-height: 29.4px;
    text-transform: uppercase;
    letter-spacing: -0.2px;
  }
  .core-values li {
    display: flex;
    align-items: center;
    gap: 9px;
  }
  .core-values li::before {
    content: "";
    width: 0;
    height: 0;
    border-top: 7px solid transparent;
    border-bottom: 7px solid transparent;
    border-left: 12px solid var(--brand-red);
  }
  .core-values li:nth-child(odd) { color: var(--text-white); }
  .core-values li:nth-child(even) { color: var(--text-grey); }
  .mission {
    position: absolute;
    left: 24px;
    top: 226px;
    width: 570px;
    color: var(--brand-red);
    font-size: 31px;
    line-height: 35.5px;
    text-transform: uppercase;
    letter-spacing: -0.2px;
  }
  .brand-name {
    position: absolute;
    left: 530px;
    top: 80px;
    width: 180px;
    text-align: center;
    color: var(--brand-red);
    font-size: 40px;
    line-height: 44px;
    text-transform: uppercase;
  }
  .truck-photo {
    position: absolute;
    left: 710px;
    top: 75px;
    width: 450px;
    height: 250px;
    background: radial-gradient(ellipse at 45% 55%, var(--photo-light) 0%, #8a8a8a 45%, var(--photo-dark) 100%);
    border-radius: 6px;
  }
</style>
</head>
<body>
  <section class="banner">
    <svg class="banner__accent" viewBox="0 0 1160 387" preserveAspectRatio="none" aria-hidden="true">
      <polygon points="851,0 1160,0 1160,387 677,387" fill="var(--brand-red-dark)"/>
      <polygon points="870,0 1160,0 1160,387 772,387" fill="var(--brand-red)"/>
    </svg>

    <ul class="core-values">
      <li>Do the right things for the right reasons</li>
      <li>Pursue growth and development</li>
      <li>Build a positive team atmosphere</li>
      <li>Deliver wow through service</li>
      <li>Do everything safely</li>
      <li>Have fun</li>
    </ul>

    <p class="mission">Provide the best customer experience while creating an environment of growth and opportunity for our customers, employees, and service providers.</p>

    <div class="brand-name">TEK Logistics</div>

    <div class="truck-photo" role="img" aria-label="Photo of a chrome semi-truck with a white trailer"></div>
  </section>
</body>
</html>
```